Compnay PowerPoint Tempalte Design

I am needing a good base design and slide designs for interior and exterior company presentations. The template will need to be on the company brand with proper coloring and fonts. Able to be creative with layout options with a good example attached.
website for reference: www.crewvantor.com/

Target Market(s)

Professionals

Font styles to use
Other font styles liked:
• Helvetica

Requirements
Must have
• On Brand Colors, Clean, simple design

```html
<!DOCTYPE html>
<html lang="en">
<head>
<meta charset="utf-8">
<title>Crewvantor Presentation Template</title>
<link href="https://fonts.googleapis.com/css2?family=Arimo:wght@400;700&display=swap" rel="stylesheet">
<style>
:root{
  --bg:#c9c8ca;
  --teal:#4aa89e;
  --teal-dark:#2f8a8f;
  --blue:#2a8ab5;
  --ink:#111;
  --grey-text:#555;
  --footer:#333;
  --white:#fff;
}
*{margin:0;padding:0;box-sizing:border-box}
html,body{width:688px;height:1200px;overflow:hidden;background:var(--bg);font-family:"Arimo",Helvetica,Arial,sans-serif;color:var(--ink)}
.canvas{position:relative;width:688px;height:1200px}
.slide{position:absolute;width:310px;height:174px;overflow:hidden;background:var(--white)}
.slide svg.art{position:absolute;left:0;top:0;width:310px;height:174px}
.hero{left:128px;top:51px;transform:scale(1.3935);transform-origin:0 0}
.abs{position:absolute;white-space:nowrap}
.url{left:26px;top:13px;font-size:4.4px;color:#777;letter-spacing:.1px}
.url b{color:var(--teal);font-weight:400}
.tagline{left:26px;top:10px;font-size:4px;color:#888;line-height:4.6px;white-space:normal;width:170px}
.brand{right:20px;top:44px;font-size:8px;font-weight:700;color:var(--ink);letter-spacing:.3px}
.title-main{left:27px;top:62px;font-size:17.5px;font-weight:700;line-height:18px}
.title-sub{left:27px;top:81px;font-size:17px;line-height:18px}
.title-rule{left:27px;top:100px;width:140px;height:1.2px;background:var(--white)}
.subtitle{left:27px;top:104px;font-size:8.4px}
.date{left:27px;top:130px;font-size:4.4px}
.on-dark .title-main,.on-dark .title-sub,.on-dark .subtitle,.on-dark .date{color:var(--white)}
.footer-bar{left:0;bottom:0;width:310px;height:9px;background:var(--footer);color:var(--white);font-size:3px;text-align:center;line-height:9px}
.bottom-brand{left:6px;top:158px;font-size:4.2px;font-weight:700}
.bottom-band{left:26px;top:161px;width:284px;height:5px;background:linear-gradient(90deg,var(--teal),var(--blue));color:var(--white);font-size:2.3px;line-height:5px;text-align:right;padding-right:6px}
.section-title{font-size:13px;font-weight:700}
.body-copy{font-size:4.6px;line-height:5.5px;color:#333;white-space:normal}
.band-title{left:0;width:310px;text-align:center;font-size:11.5px;font-weight:700;color:var(--white)}
.band-mark{width:6px;height:6px;background:var(--white);left:152px}
.member{width:84px;text-align:center;top:96px}
.member .name{font-size:6px;font-weight:700;color:var(--teal)}
.member .role{font-size:4px;margin-top:1px}
.member .bio{font-size:3.8px;line-height:4.6px;margin-top:5px;white-space:normal}
.value{width:64px;text-align:center;top:95px}
.value .head{font-size:6px;font-weight:700;color:var(--teal);padding-bottom:2px;border-bottom:.5px solid #aaa}
.value .text{font-size:3.9px;line-height:4.6px;margin-top:3px;white-space:normal}
.contact-brand{left:31px;top:78px;font-size:9px;font-weight:700;color:var(--white)}
.contact-head{left:31px;top:96px;font-size:6px;font-weight:700;color:var(--white)}
.contact-row{left:31px;font-size:4.2px;color:var(--white);display:flex;align-items:center;gap:4px}
.contact-row svg{width:5px;height:5px}
</style>
</head>
<body>
<svg width="0" height="0" style="position:absolute" aria-hidden="true">
  <defs>
    <linearGradient id="tealPhoto" x1="0" y1="0" x2="1" y2="1">
      <stop offset="0" stop-color="#5fb8ac"/><stop offset=".55" stop-color="#3f9c97"/><stop offset="1" stop-color="#3187a3"/>
    </linearGradient>
    <linearGradient id="darkPhoto" x1="0" y1="0" x2="1" y2="1">
      <stop offset="0" stop-color="#2a3b42"/><stop offset=".5" stop-color="#2c5a64"/><stop offset="1" stop-color="#3a8c92"/>
    </linearGradient>
    <linearGradient id="accentLine" x1="0" y1="0" x2="1" y2="0">
      <stop offset="0" stop-color="#4aa89e"/><stop offset="1" stop-color="#d9efee"/>
    </linearGradient>
  </defs>
</svg>

<div class="canvas">

  <!-- Hero title slide -->
  <section class="slide hero">
    <svg class="art" viewBox="0 0 310 174">
      <g role="img" aria-label="Photo of a smiling group of young colleagues, tinted teal">
        <polygon points="0,37 239,37 265,63 310,63 310,165 0,165" fill="url(#tealPhoto)"/>
      </g>
      <polyline points="0,32.5 240,32.5 268,60.5 310,60.5" fill="none" stroke="url(#accentLine)" stroke-width="2.5"/>
    </svg>
    <div class="abs url">https://www.<b>crewvantor</b>.com</div>
    <div class="abs brand">CREWVANTOR</div>
    <div class="abs title-main">PRESENTATION</div>
    <div class="abs title-sub">Title Goes Here!</div>
    <div class="abs title-rule"></div>
    <div class="abs subtitle">Subtitle of Presentation Goes Here!</div>
    <div class="abs date">September 27, 2021</div>
    <div class="abs footer-bar">Copyright 2021 Crewvantor. All rights reserved</div>
  </section>

  <!-- Title variant: teal, group -->
  <section class="slide" style="left:29px;top:442px">
    <svg class="art" viewBox="0 0 310 174">
      <g role="img" aria-label="Photo of a group of colleagues, tinted teal">
        <polygon points="0,37 239,37 265,63 310,63 310,165 0,165" fill="url(#tealPhoto)"/>
      </g>
      <polyline points="0,32.5 240,32.5 268,60.5 310,60.5" fill="none" stroke="url(#accentLine)" stroke-width="2.5"/>
    </svg>
    <div class="abs url">https://www.<b>crewvantor</b>.com</div>
    <div class="abs brand">CREWVANTOR</div>
    <div class="abs title-main">PRESENTATION</div>
    <div class="abs title-sub">Title Goes Here!</div>
    <div class="abs subtitle">Subtitle of Presentation Goes Here!</div>
    <div class="abs date">September 27, 2021</div>
    <div class="abs footer-bar">Copyright 2021 Crewvantor. All rights reserved</div>
  </section>

  <!-- Title variant: dark, office -->
  <section class="slide on-dark" style="left:349px;top:442px">
    <svg class="art" viewBox="0 0 310 174">
      <g role="img" aria-label="Photo of a man working at a laptop in an office, tinted dark teal">
        <polygon points="0,37 239,37 265,63 310,63 310,165 0,165" fill="url(#darkPhoto)"/>
      </g>
      <polyline points="0,32.5 240,32.5 268,60.5 310,60.5" fill="none" stroke="url(#accentLine)" stroke-width="2.5"/>
    </svg>
    <div class="abs url">https://www.<b>crewvantor</b>.com</div>
    <div class="abs brand">CREWVANTOR</div>
    <div class="abs title-main">PRESENTATION</div>
    <div class="abs title-sub">Title Goes Here!</div>
    <div class="abs subtitle">Subtitle of Presentation Goes Here!</div>
    <div class="abs date">September 27, 2021</div>
    <div class="abs footer-bar">Copyright 2021 Crewvantor. All rights reserved</div>
  </section>

  <!-- Title variant: teal, cafe, tagline -->
  <section class="slide" style="left:29px;top:627px">
    <svg class="art" viewBox="0 0 310 174">
      <g role="img" aria-label="Photo of friends chatting over coffee, tinted teal">
        <polygon points="0,37 239,37 265,63 310,63 310,165 0,165" fill="url(#tealPhoto)"/>
      </g>
      <polyline points="0,32.5 240,32.5 268,60.5 310,60.5" fill="none" stroke="url(#accentLine)" stroke-width="2.5"/>
    </svg>
    <div class="abs tagline">Where we maintain a passion for excellence, striving to be better each and every day, so that our guests leave happy and our team members feel fulfilled.</div>
    <div class="abs brand">CREWVANTOR</div>
    <div class="abs title-main">PRESENTATION</div>
    <div class="abs title-sub">Title Goes Here!</div>
    <div class="abs subtitle">Subtitle of Presentation Goes Here!</div>
    <div class="abs date">September 27, 2021</div>
    <div class="abs footer-bar">Copyright 2021 Crewvantor. All rights reserved</div>
  </section>

  <!-- Title variant: dark, city -->
  <section class="slide on-dark" style="left:349px;top:627px">
    <svg class="art" viewBox="0 0 310 174">
      <g role="img" aria-label="Aerial photo of city buildings, tinted dark teal">
        <polygon points="0,37 239,37 265,63 310,63 310,165 0,165" fill="url(#darkPhoto)"/>
      </g>
      <polyline points="0,32.5 240,32.5 268,60.5 310,60.5" fill="none" stroke="url(#accentLine)" stroke-width="2.5"/>
    </svg>
    <div class="abs tagline">Where we maintain a passion for excellence, striving to be better each and every day, so that our guests leave happy and our team members feel fulfilled.</div>
    <div class="abs brand">CREWVANTOR</div>
    <div class="abs title-main">PRESENTATION</div>
    <div class="abs title-sub">Title Goes Here!</div>
    <div class="abs subtitle">Subtitle of Presentation Goes Here!</div>
    <div class="abs date">September 27, 2021</div>
    <div class="abs footer-bar">Copyright 2021 Crewvantor. All rights reserved</div>
  </section>

  <!-- About Us -->
  <section class="slide" style="left:29px;top:811px">
    <div class="abs" style="left:142px;top:32px;width:136px;height:90px;background:var(--teal)"></div>
    <div class="abs" role="img" aria-label="Photo of women laughing together at a cafe table" style="left:147px;top:38px;width:137px;height:85px;background:linear-gradient(135deg,#4a3a30,#8a6a55 55%,#c9b6a4)"></div>
    <div class="abs" style="left:151px;top:42px;width:138px;height:86px;border:1px solid var(--teal);border-top:none;border-left-color:transparent"></div>
    <div class="abs section-title" style="left:23px;top:50px">About Us</div>
    <div class="abs body-copy" style="left:23px;top:68px;width:114px">Crewvantor is dedicated to cultivating a positive culture of leadership for its team members' professional and personal development, and this person-focused mentality transfers throughout the company from partners to our teams to guests. We strive to ensure each team member feels valued in all aspects of their role, reinforcing the importance of fostering a self-sustaining culture of success where everyone makes a team effort to communicate and overcome adversity.</div>
    <div class="abs bottom-brand">CREWVANTOR</div>
    <div class="abs bottom-band">Copyright 2021 Crewvantor. All rights reserved &nbsp;|&nbsp; 5</div>
  </section>

  <!-- Meet The Team -->
  <section class="slide" style="left:349px;top:811px">
    <div class="abs" role="img" aria-label="Photo of colleagues in an office, tinted teal" style="left:0;top:0;width:310px;height:72px;background:linear-gradient(100deg,#5fb5aa,#3f9a96 60%,#3a8fa8)"></div>
    <div class="abs band-title" style="top:26px">Meet The Team</div>
    <div class="abs" role="img" aria-label="Portrait of the CEO" style="left:47px;top:50px;width:44px;height:44px;border-radius:50%;border:1.5px solid #fff;background:linear-gradient(#8d9aa3,#2f3f55)"></div>
    <div class="abs" role="img" aria-label="Portrait of the controller" style="left:133px;top:50px;width:44px;height:44px;border-radius:50%;border:1.5px solid #fff;background:linear-gradient(#c9a58a,#6b4a38)"></div>
    <div class="abs" role="img" aria-label="Portrait of the COO" style="left:218px;top:50px;width:44px;height:44px;border-radius:50%;border:1.5px solid #fff;background:linear-gradient(#9ab0c8,#2856a8)"></div>
    <div class="abs member" style="left:27px"><div class="name">EVAN MARLOW</div><div class="role">CEO</div><div class="bio">Lorem ipsum dolor sit amet, consectetur adipiscing elit. Vivamus eu dui ex. Curabitur dapibus dignissim dui, in molestie metus feugiat sed.</div></div>
    <div class="abs member" style="left:113px"><div class="name">NORA HALVEY</div><div class="role">CONTROLLER</div><div class="bio">Lorem ipsum dolor sit amet, consectetur adipiscing elit. Vivamus eu dui ex. Curabitur dapibus dignissim dui, in molestie metus feugiat sed.</div></div>
    <div class="abs member" style="left:198px"><div class="name">REID CASTELL</div><div class="role">COO</div><div class="bio">Lorem ipsum dolor sit amet, consectetur adipiscing elit. Vivamus eu dui ex. Curabitur dapibus dignissim dui, in molestie metus feugiat sed.</div></div>
    <div class="abs bottom-brand">CREWVANTOR</div>
    <div class="abs bottom-band">Copyright 2021 Crewvantor. All rights reserved &nbsp;|&nbsp; 6</div>
  </section>

  <!-- Our Core Values -->
  <section class="slide" style="left:29px;top:995px">
    <div class="abs" role="img" aria-label="Photo of a smiling group, tinted teal" style="left:0;top:0;width:310px;height:87px;background:linear-gradient(100deg,#5fb5aa,#3f9a96 60%,#3a8fa8)"></div>
    <div class="abs band-title" style="top:26px">Our Core Values</div>
    <div class="abs body-copy" style="left:38px;top:53px;width:234px;text-align:center;color:#fff;font-size:5px;line-height:6px">Our culture is founded on four core values and the entrepreneurial spirit of ownership that comes from a foundation of passion for our people, commitment to our business, transparency, and continued progress.</div>
    <div class="abs" style="left:45px;top:84px;width:6px;height:6px;background:#fff;border:.6px solid var(--teal)"></div>
    <div class="abs" style="left:116px;top:84px;width:6px;height:6px;background:#fff;border:.6px solid var(--teal)"></div>
    <div class="abs" style="left:187px;top:84px;width:6px;height:6px;background:#fff;border:.6px solid var(--teal)"></div>
    <div class="abs" style="left:258px;top:84px;width:6px;height:6px;background:#fff;border:.6px solid var(--teal)"></div>
    <div class="abs value" style="left:16px"><div class="head">INTEGRITY</div><div class="text">Integrity in everything we do. Do the right thing, even when no one is looking.</div></div>
    <div class="abs value" style="left:87px"><div class="head">FAMILY</div><div class="text">Family first, always. All decisions must benefit our family and the company.</div></div>
    <div class="abs value" style="left:158px"><div class="head">RESPECT</div><div class="text">We care for one another, praise efforts, recognize progress, and reward results.</div></div>
    <div class="abs value" style="left:229px"><div class="head">PASSION</div><div class="text">We are positive, hardworking, and disciplined in all we do, which stems from our innate passion.</div></div>
    <div class="abs bottom-brand">CREWVANTOR</div>
    <div class="abs bottom-band">Copyright 2021 Crewvantor. All rights reserved &nbsp;|&nbsp; 7</div>
  </section>

  <!-- Contact -->
  <section class="slide" style="left:349px;top:995px">
    <div class="abs" role="img" aria-label="Aerial photo of city streets and buildings, tinted dark teal" style="left:0;top:0;width:310px;height:165px;background:linear-gradient(120deg,#2a3b42,#2c5a64 50%,#3a8c92)"></div>
    <div class="abs contact-brand">CREWVANTOR</div>
    <div class="abs contact-head">Contact Us</div>
    <div class="abs contact-row" style="top:110px">
      <svg viewBox="0 0 10 10"><path d="M2 1l2 2-1 1.5c.8 1.5 1.5 2.2 3 3L7.5 6l2 2-1.5 1.5C4.5 9 1 5.5.5 2z" fill="#fff"/></svg>4455-0100-2736</div>
    <div class="abs contact-row" style="top:119px">
      <svg viewBox="0 0 10 10"><circle cx="5" cy="5" r="4" fill="none" stroke="#fff"/><circle cx="5" cy="5" r="1.6" fill="none" stroke="#fff"/></svg>info@crewvantor.com</div>
    <div class="abs contact-row" style="top:128px">
      <svg viewBox="0 0 10 10"><circle cx="5" cy="5" r="4" fill="none" stroke="#fff" stroke-width=".8"/><ellipse cx="5" cy="5" rx="1.8" ry="4" fill="none" stroke="#fff" stroke-width=".8"/><path d="M1 5h8" stroke="#fff" stroke-width=".8"/></svg>www.crewvantor.com</div>
    <div class="abs footer-bar">Copyright 2021 Crewvantor. All rights reserved</div>
  </section>

</div>
</body>
</html>
```